Brightpath Health Flyer Design for Virtual Online Clinic. -5.5 x 8.5 inches (half sheet)

We need a clean, modern flyer design for Brightpath Health, a new virtual walk-in clinic based in British Columbia. The flyer will be used in libraries, pharmacies, and community centers to help residents easily access primary care through their Brightpath Health NFC access card.
The flyer will ask a question : NEED A DOCTOR? This should be large and attention grabbing.
The design should clearly feature a Brightpath Health card image (the access card) as the centerpiece and visually show how patients can use it to book appointments. The tone should feel trustworthy, healthcare-oriented, and community-friendly — clean fonts, clear spacing, and strong readability from a distance.

Side One: This card has the NFC Access Card.
NEED A DOCTOR? (Large Font, Attention Grabbing)
How to Book an Appointment using your Brightpath Health Card
Step 1: Tap Your Card on Your Phone
Hold your card near the back of your phone.
It will activate automatically — no app needed.
The Brightpath Health scheduler will open.
Step 2: Schedule Your Appointment
Select your clinical concern.
Choose your time window.
Register (only once).
Confirm your appointment.
Step 3: Relax, we’ll take care of the rest
A doctor will call during your scheduled time.
Once booked, you’ll be able to call our office.
No emails, no texts — just a real person.
It’s that simple.
Side Two:
About Brightpath Health
Created by Dr. Marcus Feldtree
Brightpath Health was founded to make healthcare simple and convenient. Prescription renewals. Common infections. Medical notes. And so much more.
Our doctors can address 120+ health concerns virtually — providing quality care without the waiting room. No waiting rooms. Just real doctors providing real care.
Why Patients Choose Brightpath Health
Easy access – book and be seen from anywhere in BC.
Effortless booking – tap your Brightpath Health Card to begin.
Trusted physicians – every visit is with a licensed BC family doctor.
How It Works
Book your visit — choose a time window that fits your day.
Join the queue — you’ll be called when it’s your turn.
Speak directly with your doctor — simple, secure, and stress-free.
Convenient Care for Common Concerns

Additional Details.
Please find the domain to be launched soon. I've attached the NFC card file for review, it is 85.5 mm x 54 mm. The card will be glued to the flyer.
I've attached examples of flyers but they are not the look I am seeking and I am looking for creative solutions.
Thank you!
http://brightpath-example.test/

Target Market(s)

Adult Patients in British Columbia

Industry/Entity Type

Healthcare

Font styles to use
Other font styles liked:
• Looking for clean lines, uniform appearance, and high legibility i.e poppins

Colors
0054AA
0677BA
7BADD7
CADEEF
E8F1F8

Requirements
Must have
• Need A Doctor?
Nice to have
• Elegant style, not too busy, clear layout.
Should not have
• Clutter, look cheap - review examples.

```html
<!DOCTYPE html>
<html lang="en">
<head>
<meta charset="utf-8">
<title>Brightpath Health – Need a Doctor? Flyer</title>
<link rel="stylesheet" href="https://fonts.googleapis.com/css2?family=Poppins:wght@400;500;600;700;800&display=swap">
<style>
  :root {
    --brand-blue: #2a3f9e;
    --brand-blue-dark: #1f3187;
    --brand-blue-mid: #4a63b8;
    --brand-blue-pale: #e8f1f8;
    --ink-dark: #2e2e2e;
    --ink-sub: #444444;
    --ink-body: #333a45;
    --rule: #3a3a3a;
    --accent-yellow: #f1e98a;
    --page-bg: #ececec;
    --sheet: #ffffff;
  }
  * { box-sizing: border-box; margin: 0; padding: 0; }
  html, body {
    width: 1200px; height: 1200px; overflow: hidden;
    background: var(--page-bg);
    font-family: "Poppins", sans-serif;
  }
  .flyer {
    position: absolute; left: 230px; top: 28px;
    width: 740px; height: 1144px;
    background: var(--sheet);
    overflow: hidden;
  }
  .corner-texture { position: absolute; top: 0; width: 250px; height: 130px; }
  .corner-texture--left { left: 0; background: radial-gradient(ellipse at top left, rgba(150,150,160,.28), rgba(255,255,255,0) 70%); }
  .corner-texture--right { right: 0; background: radial-gradient(ellipse at top right, rgba(150,150,160,.28), rgba(255,255,255,0) 70%); }

  .brand {
    position: absolute; top: 66px; left: 0; width: 100%;
    display: flex; justify-content: center; align-items: center; gap: 12px;
    color: var(--brand-blue);
    font-size: 30px; font-weight: 500; line-height: 40px; letter-spacing: .5px;
  }
  .brand__dot { width: 14px; height: 14px; border-radius: 50%; background: var(--brand-blue); }

  .headline { position: absolute; top: 118px; left: 0; width: 100%; text-align: center; }
  .headline__lead {
    display: block; color: var(--ink-dark);
    font-size: 76px; font-weight: 800; line-height: 74px; letter-spacing: -1px;
  }
  .headline__main {
    display: block; color: var(--brand-blue);
    font-size: 110px; font-weight: 800; line-height: 104px; letter-spacing: -3px;
  }
  .tagline {
    position: absolute; top: 302px; left: 0; width: 100%; text-align: center;
    color: var(--ink-sub); font-size: 25px; font-weight: 600; line-height: 30px; letter-spacing: .3px;
  }

  .card-visual {
    position: absolute; left: 60px; top: 352px; width: 620px; height: 320px;
    background: radial-gradient(ellipse 48% 44% at 50% 50%, var(--brand-blue-mid) 0%, #8a9bd3 45%, var(--brand-blue-pale) 75%, var(--sheet) 100%);
  }

  .frame {
    position: absolute; left: 14px; right: 14px; top: 470px; bottom: 36px;
    border: 1.2px solid var(--rule); border-top: none;
  }

  .section-title {
    position: absolute; top: 698px; left: 0; width: 100%; text-align: center;
    color: var(--brand-blue); font-size: 22px; font-weight: 700; line-height: 29px;
    letter-spacing: .2px;
  }
  .section-title__underline { position: absolute; top: 758px; left: 190px; }

  .steps { position: absolute; top: 792px; left: 0; width: 100%; height: 100px; }
  .steps__link { position: absolute; top: 49px; height: 1.5px; background: var(--rule); width: 128px; }
  .step-badge { position: absolute; top: 0; width: 100px; height: 100px; }
  .step-badge__label {
    position: absolute; inset: 0; display: flex; align-items: center; justify-content: center;
    color: #fff; font-size: 21px; font-weight: 700;
  }

  .step-columns {
    position: absolute; top: 905px; left: 30px; right: 14px;
    display: grid; grid-template-columns: 1fr 1fr 1fr;
  }
  .step-column { list-style: none; padding: 0 10px 0 12px; border-left: 1.2px solid #666; min-height: 125px; }
  .step-column:first-child { border-left: none; }
  .step-column__item {
    position: relative; padding-left: 12px; margin-bottom: 12px;
    color: var(--ink-body); font-size: 11.6px; font-weight: 500; line-height: 1.3;
  }
  .step-column__item::before {
    content: ""; position: absolute; left: 0; top: 4px;
    border-left: 5px solid var(--brand-blue);
    border-top: 3.5px solid transparent; border-bottom: 3.5px solid transparent;
  }

  .site-url {
    position: absolute; bottom: 22px; left: 50%; transform: translateX(-50%);
    padding: 0 20px; background: var(--sheet);
    color: var(--brand-blue); font-size: 23px; font-weight: 500; white-space: nowrap;
  }
  .site-url strong { font-weight: 700; }
  .step-ring { stroke-dasharray: 10 6 10 6 10 6 10 6 10 6 0 200; }
</style>
</head>
<body>
<main class="flyer">
  <div class="corner-texture corner-texture--left" role="img" aria-label="Faint grey square dot texture fading from the corner"></div>
  <div class="corner-texture corner-texture--right" role="img" aria-label="Faint grey square dot texture fading from the corner"></div>

  <div class="brand"><span class="brand__dot"></span>Brightpath Health</div>

  <h1 class="headline">
    <span class="headline__lead">NEED A</span>
    <span class="headline__main">DOCTOR?</span>
  </h1>
  <p class="tagline">THIS CARD HAS THE NFC ACCESS CARD</p>

  <div class="frame"></div>

  <div class="card-visual" role="img" aria-label="Illustration of the blue and white Brightpath Health NFC access cards, front and back"></div>

  <h2 class="section-title">HOW TO BOOK AN APPOINTMENT USING<br>YOUR BRIGHTPATH HEALTH CARD</h2>
  <svg class="section-title__underline" width="360" height="14" viewBox="0 0 360 14" aria-hidden="true">
    <path d="M2 9 C90 4 250 3 358 8" stroke="var(--accent-yellow)" stroke-width="2" fill="none"/>
    <path d="M60 12 C150 8 260 8 340 10" stroke="var(--accent-yellow)" stroke-width="1.4" fill="none"/>
  </svg>

  <div class="steps">
    <div class="steps__link" style="left:246px"></div>
    <div class="steps__link" style="left:492px"></div>

    <div class="step-badge" style="left:128px">
      <svg width="100" height="100" viewBox="0 0 100 100" aria-hidden="true">
        <circle cx="50" cy="50" r="40" fill="var(--brand-blue)"/>
        <circle class="step-ring" cx="50" cy="50" r="46" fill="none" stroke="var(--ink-dark)" stroke-width="3" pathLength="200" transform="rotate(-90 50 50)"/>
      </svg>
      <span class="step-badge__label">STEP 1</span>
    </div>
    <div class="step-badge" style="left:374px">
      <svg width="100" height="100" viewBox="0 0 100 100" aria-hidden="true">
        <circle cx="50" cy="50" r="40" fill="var(--brand-blue)"/>
        <circle class="step-ring" cx="50" cy="50" r="46" fill="none" stroke="var(--ink-dark)" stroke-width="3" pathLength="200" transform="rotate(-90 50 50)"/>
      </svg>
      <span class="step-badge__label">STEP 2</span>
    </div>
    <div class="step-badge" style="left:620px">
      <svg width="100" height="100" viewBox="0 0 100 100" aria-hidden="true">
        <circle cx="50" cy="50" r="40" fill="var(--brand-blue)"/>
        <circle class="step-ring" cx="50" cy="50" r="46" fill="none" stroke="var(--ink-dark)" stroke-width="3" pathLength="200" transform="rotate(-90 50 50)"/>
      </svg>
      <span class="step-badge__label">STEP 3</span>
    </div>
  </div>

  <div class="step-columns">
    <ul class="step-column">
      <li class="step-column__item">Tap Your Card on Your Phone</li>
      <li class="step-column__item">Hold your card near the back of your phone.</li>
      <li class="step-column__item">It will activate automatically — no app needed.</li>
      <li class="step-column__item">The Brightpath Health scheduler will open.</li>
    </ul>
    <ul class="step-column">
      <li class="step-column__item">Schedule Your Appointment</li>
      <li class="step-column__item">Select your clinical concern.</li>
      <li class="step-column__item">Choose your time window.</li>
      <li class="step-column__item">Register (only once).</li>
      <li class="step-column__item">Confirm your appointment.</li>
    </ul>
    <ul class="step-column">
      <li class="step-column__item">Relax, we’ll take care of the rest<br>A doctor will call during your scheduled time.</li>
      <li class="step-column__item">Once booked, you’ll be able to call our office.</li>
      <li class="step-column__item">No emails, no texts — just a real person. It’s that simple.</li>
    </ul>
  </div>

  <p class="site-url">www.<strong>brightpath-example</strong>.test</p>
</main>
</body>
</html>
```